Finance cashflow waterfall graphic

Recreate "Cashflow Waterfall Example 1" - waterfall term used to explain the different accounts and priority that need to be paid as part of a apartment building / project. Create simple, business professional graphic for real estate report. Check the inspiration image but change to dorm building, no people - potentially combine the two images... Ideally editable so I can change the names of the accounts / colors / etc.

```html
<!DOCTYPE html>
<html lang="en">
<head>
<meta charset="utf-8">
<title>Cashflow Waterfall</title>
<link href="https://fonts.googleapis.com/css2?family=Roboto+Condensed:wght@500;700&display=swap" rel="stylesheet">
<style>
  :root {
    --bg: #ffffff;
    --ground: #9fbf4a;
    --barrel-light: #d9663c;
    --barrel-dark: #a8442a;
    --building-main: #f6a864;
    --building-roof: #22527a;
    --tap: #b9b9bb;
    --water: #6bb8e6;
    --tag-dark: #9b9b9b;
    --tag-light: #ffffff;
    --ink: #111111;
    --on-barrel: #ffffff;
  }
  html, body {
    margin: 0;
    padding: 0;
    background: var(--bg);
    overflow: hidden;
  }
  .waterfall {
    display: block;
    width: 1200px;
    height: 927px;
  }
  .ground { fill: var(--ground); }
  .tap { fill: var(--tap); }
  .stream { stroke: var(--water); stroke-width: 3; }
  .tag-label {
    font-family: "Roboto Condensed", "Arial Narrow", sans-serif;
    font-weight: 500;
    font-size: 13.5px;
    fill: var(--ink);
    text-anchor: middle;
    dominant-baseline: middle;
  }
  .tag-label--lead { font-size: 21px; font-weight: 500; }
  .share {
    font-family: "Roboto Condensed", "Arial Narrow", sans-serif;
    font-weight: 700;
    font-size: 18px;
    fill: var(--on-barrel);
    text-anchor: middle;
    dominant-baseline: middle;
  }
</style>
</head>
<body>
<svg class="waterfall" viewBox="0 0 1200 927" xmlns="http://www.w3.org/2000/svg">
  <defs>
    <linearGradient id="tag-fill" x1="0" x2="1" y1="0" y2="0">
      <stop offset="0" stop-color="var(--tag-dark)"/>
      <stop offset="1" stop-color="var(--tag-light)"/>
    </linearGradient>
    <linearGradient id="tag-fill-rev" x1="1" x2="0" y1="0" y2="0">
      <stop offset="0" stop-color="var(--tag-dark)"/>
      <stop offset="1" stop-color="var(--tag-light)"/>
    </linearGradient>
    <linearGradient id="barrel-fill" x1="0" x2="1" y1="0" y2="0">
      <stop offset="0" stop-color="var(--barrel-dark)"/>
      <stop offset="0.5" stop-color="var(--barrel-light)"/>
      <stop offset="1" stop-color="var(--barrel-dark)"/>
    </linearGradient>
    <linearGradient id="building-fill" x1="0" x2="0" y1="0" y2="1">
      <stop offset="0" stop-color="var(--building-main)"/>
      <stop offset="1" stop-color="#eeb48a"/>
    </linearGradient>
  </defs>

  <!-- ground pads -->
  <g class="grounds">
    <rect class="ground" x="58" y="343" width="370" height="33" rx="16"/>
    <rect class="ground" x="406" y="445" width="122" height="26" rx="13"/>
    <rect class="ground" x="512" y="533" width="108" height="24" rx="12"/>
    <rect class="ground" x="608" y="613" width="94" height="21" rx="10"/>
    <rect class="ground" x="696" y="683" width="80" height="18" rx="9"/>
    <rect class="ground" x="772" y="755" width="80" height="18" rx="9"/>
    <rect class="ground" x="849" y="826" width="167" height="19" rx="9"/>
  </g>

  <!-- dorm building -->
  <g class="building" role="img" aria-label="Illustration of a multi-storey dorm building with windows and a red front door">
    <rect x="101" y="71" width="196" height="11" fill="var(--building-roof)"/>
    <rect x="112" y="82" width="174" height="292" fill="url(#building-fill)"/>
  </g>

  <!-- water streams -->
  <g class="streams">
    <line class="stream" x1="355" y1="234" x2="355" y2="280"/>
    <line class="stream" x1="465" y1="342" x2="465" y2="383"/>
    <line class="stream" x1="563" y1="440" x2="563" y2="478"/>
    <line class="stream" x1="653" y1="528" x2="653" y2="563"/>
    <line class="stream" x1="734" y1="607" x2="734" y2="640"/>
    <line class="stream" x1="810" y1="681" x2="810" y2="712"/>
    <line class="stream" x1="886" y1="752" x2="886" y2="782"/>
  </g>

  <!-- barrels -->
  <g class="barrels">
    <rect role="img" aria-label="Wooden barrel filled with water" x="305" y="276" width="104" height="91" rx="6" fill="url(#barrel-fill)"/>
    <rect role="img" aria-label="Wooden barrel filled with water" x="419" y="379" width="95" height="81" rx="6" fill="url(#barrel-fill)"/>
    <rect role="img" aria-label="Wooden barrel filled with water" x="522" y="474" width="87" height="73" rx="5" fill="url(#barrel-fill)"/>
    <rect role="img" aria-label="Wooden barrel filled with water" x="616" y="559" width="79" height="67" rx="5" fill="url(#barrel-fill)"/>
    <rect role="img" aria-label="Wooden barrel filled with water" x="701" y="636" width="69" height="59" rx="4" fill="url(#barrel-fill)"/>
    <rect role="img" aria-label="Wooden barrel filled with water" x="776" y="708" width="71" height="59" rx="4" fill="url(#barrel-fill)"/>
    <rect role="img" aria-label="Wooden barrel holding the 60 percent share" x="855" y="778" width="68" height="60" rx="4" fill="url(#barrel-fill)"/>
    <rect role="img" aria-label="Wooden barrel holding the 40 percent share" x="940" y="778" width="68" height="60" rx="4" fill="url(#barrel-fill)"/>
  </g>

  <!-- taps -->
  <g class="taps">
    <rect class="tap" role="img" aria-label="Water tap" x="286" y="192" width="74" height="42" rx="5"/>
    <rect class="tap" role="img" aria-label="Water tap" x="403" y="305" width="66" height="37" rx="5"/>
    <rect class="tap" role="img" aria-label="Water tap" x="505" y="406" width="62" height="34" rx="5"/>
    <rect class="tap" role="img" aria-label="Water tap" x="603" y="497" width="54" height="31" rx="4"/>
    <rect class="tap" role="img" aria-label="Water tap" x="690" y="580" width="47" height="27" rx="4"/>
    <rect class="tap" role="img" aria-label="Water tap" x="766" y="653" width="48" height="28" rx="4"/>
    <rect class="tap" role="img" aria-label="Water tap" x="842" y="724" width="48" height="28" rx="4"/>
  </g>

  <!-- account tags -->
  <g class="tags">
    <polygon points="220,312 384,312 396,325.5 384,339 220,339 234,325.5" fill="url(#tag-fill)"/>
    <text class="tag-label tag-label--lead" x="310" y="327">REVENUE</text>

    <polygon points="295,411 459,411 471,424.5 459,438 295,438 309,424.5" fill="url(#tag-fill)"/>
    <text class="tag-label" x="386" y="425">Operating Expenses</text>

    <polygon points="393,501 558,501 570,514 558,527 393,527 407,514" fill="url(#tag-fill)"/>
    <text class="tag-label" x="485" y="515">Debt Payment</text>

    <polygon points="482,582 647,582 659,595.5 647,609 482,609 496,595.5" fill="url(#tag-fill)"/>
    <text class="tag-label" x="574" y="596">Asset Management Fees</text>

    <polygon points="562,653 727,653 739,667 727,681 562,681 576,667" fill="url(#tag-fill)"/>
    <text class="tag-label" x="653" y="668">Recapitalization Accounts</text>

    <polygon points="639,725 804,725 816,738.5 804,752 639,752 653,738.5" fill="url(#tag-fill)"/>
    <text class="tag-label" x="730" y="739">Incentive Fees</text>

    <polygon points="694,796 856,796 868,809.5 856,823 694,823 708,809.5" fill="url(#tag-fill)"/>
    <text class="tag-label" x="786" y="803">Sustainment Reserves/</text>
    <text class="tag-label" x="786" y="818">Member Distribution</text>

    <polygon points="1169,796 1001,796 989,809.5 1001,823 1169,823 1155,809.5" fill="url(#tag-fill-rev)"/>
    <text class="tag-label" x="1077" y="803">Private Returns/Managing</text>
    <text class="tag-label" x="1077" y="818">Member Distribution</text>
  </g>

  <!-- split shares -->
  <text class="share" x="890" y="812">60%</text>
  <text class="share" x="973" y="812">40%</text>
</svg>
</body>
</html>
```